Whisker Nana offers loving cat sitting for your precious furbaby. The industry is cat care.

This will be a website which describes cat sitting services in Marin and Sonoma Counties. The site should include, (in no particular order...I'll leave that up to the designer:
Who I AM
My Services/Rates
A Place for Reviews
Cancellation Policy
My Qualifications
Availability (client will pick from the following times) Morning 8AM- Noon or Afternoon, Noon-6PM. Anytime 8Am to 6PM. 5% discount.
Service Area (Marin & Sonoma County CA). Use Google Map
Why Book Me?
A way to pay me (through Paypal including credit card option)
A Sit Reservation Request Form
Ask Questions/ Ask for a free consult
Contact Info - name, phone, email
Vacation Services
Sign up for newsletter
I have the logo, file below. Please use complimentary colors. I have many other photos to use which I cannot seem to upload here.

```html
<!DOCTYPE html>
<html lang="en">
<head>
<meta charset="utf-8">
<title>Whisker Nana – Cat Sitting in Marin &amp; Sonoma</title>
<link href="https://fonts.googleapis.com/css2?family=Playfair+Display:ital,wght@0,600;0,700;1,600&family=Montserrat:ital,wght@0,400;0,500;0,600;0,700;1,500&display=swap" rel="stylesheet">
<style>
:root{
  --olive:#7b8b10;
  --olive-light:#9aa516;
  --plum:#4c1b2b;
  --plum-dark:#3a1220;
  --peach:#f7a77a;
  --peach-light:#fbc39f;
  --ink:#222;
  --text:#555;
  --muted:#f4f4f4;
  --white:#fff;
}
*{margin:0;padding:0;box-sizing:border-box}
html,body{width:1200px;height:4979px;overflow:hidden}
body{position:relative;font-family:'Montserrat',sans-serif;color:var(--text);background:var(--white);font-size:15px}
.abs{position:absolute}
.serif{font-family:'Playfair Display',serif;color:var(--ink);font-weight:700}
.eyebrow{font-size:12px;font-weight:500;color:var(--ink)}
.btn{position:absolute;display:flex;align-items:center;justify-content:center;gap:8px;color:#fff;font-weight:600;font-size:13px;clip-path:polygon(14px 0,calc(100% - 14px) 0,100% 50%,calc(100% - 14px) 100%,14px 100%,0 50%)}
.btn-peach{background:var(--peach)}
.btn-olive{background:var(--olive)}
.btn-pill{border-radius:30px;clip-path:none}

/* nav */
.site-nav{top:0;left:0;width:1200px;height:72px;background:#fff}
.brand{left:160px;top:23px;display:flex;align-items:center;gap:7px;font-weight:700;font-size:14px;color:var(--olive);white-space:nowrap}
.brand-dot{width:26px;height:26px;border-radius:50%;background:var(--olive);flex:none}
.nav-links{top:26px;font-size:14px;font-weight:500;color:var(--ink)}
.nav-call{left:876px;top:14px;display:flex;align-items:center;gap:10px}
.call-ring{width:44px;height:44px;border-radius:50%;background:var(--olive);border:3px solid #dfe5b8;display:flex;align-items:center;justify-content:center}
.nav-call small{display:block;font-size:12px;color:var(--ink)}
.nav-call b{font-size:15px;color:var(--plum)}

/* hero */
.hero{top:72px;left:0;width:1200px;height:643px;background:linear-gradient(100deg,#b9aea3 0%,#d8cfc6 40%,#c9beb3 70%,#a79a8e 100%);clip-path:polygon(0 0,100% 0,100% 401px,483px 643px,0 508px)}
.hero-title{left:160px;top:272px;font-size:42px;line-height:52px;color:#fff}
.hero-lead{left:160px;top:390px;width:340px;font-size:15px;line-height:23px;color:#fff}

/* reservation */
.reserve{left:684px;top:481px;width:357px;height:489px;background:var(--olive);padding:30px 22px}
.reserve h3{font-family:'Playfair Display',serif;color:#fff;font-size:22px;text-align:center;margin-bottom:20px}
.reserve label{display:block;color:#fff;font-size:12px;font-weight:700;margin-bottom:6px}
.field{background:#fff;height:41px;margin-bottom:22px;display:flex;align-items:center;justify-content:space-between;padding:0 10px;font-size:13px;color:#888}
.reserve .btn{position:relative;height:42px;margin-top:-2px}

/* contact strip */
.contact-line{left:160px;top:842px;width:412px;height:1px;background:#ddd}
.contact-line::before{content:"";position:absolute;left:0;top:-1px;width:134px;height:3px;background:var(--olive)}
.contact-item{display:flex;align-items:center;gap:10px;top:862px;font-size:14px;color:var(--ink)}
.contact-item b{display:block;color:var(--olive);font-size:14px}
.ring{width:50px;height:50px;border-radius:50%;background:var(--plum);border:4px solid #e7dde0;display:flex;align-items:center;justify-content:center;flex:none}

/* about */
.portrait{left:158px;top:937px;width:414px;height:543px;background:radial-gradient(circle at 50% 40%,#6a5a52 0%,#2a2220 45%,#0d0b0b 80%)}
.portrait-band{left:158px;top:1416px;width:414px;height:64px;background:var(--olive);clip-path:polygon(40px 0,100% 0,100% 100%,0 100%);display:flex;align-items:center;justify-content:flex-end;gap:16px;padding-right:24px;color:#fff}
.portrait-band .sig{font-family:'Playfair Display',serif;font-style:italic;font-size:24px;border-right:1px solid #fff;padding-right:16px}
.portrait-band b{display:block;font-size:14px}
.portrait-band span{font-size:11px}
.who{left:609px;top:1020px;width:432px}
.who h2{font-size:34px;margin:6px 0 10px}
.who p{font-size:15px;line-height:23px}
.checks{list-style:none;margin:14px 0 8px}
.checks li{display:flex;align-items:center;gap:10px;font-size:15px;color:var(--ink);height:31px}
.who h4{font-family:'Playfair Display',serif;font-size:15px;color:var(--plum);padding-bottom:10px;border-bottom:1px solid #ddd;margin-top:6px}
.quals{display:flex;gap:26px;margin-top:20px}
.quals div{width:203px;font-size:13px;line-height:22px}
.quals b{color:var(--ink);font-size:14px}
.cat-peek{left:1000px;top:1400px;width:182px;height:175px;background:radial-gradient(circle,#8a7f73 0%,#cfc6bb 55%,rgba(255,255,255,0) 72%)}

/* services */
.services{top:1575px;left:0;width:1200px;height:622px;background:var(--muted)}
.center{width:1200px;text-align:center;left:0}
.card{top:1723px;width:207px;height:337px;background:#fff;border:1px solid #d5d9b5}
.card-photo{height:161px;clip-path:polygon(0 0,100% 0,100% 80%,50% 100%,0 80%)}
.card-v{position:absolute;top:129px;left:0;width:207px;height:38px}
.card h3{font-family:'Playfair Display',serif;font-size:20px;color:var(--ink);text-align:center;margin-top:50px}
.card p{font-size:15px;line-height:23px;text-align:center;padding:6px 18px 0}
.card .btn{left:43px;top:324px;width:120px;height:26px;font-size:11px}

/* why */
.why-item{width:200px}
.why-item h4{font-size:17px;color:var(--ink);font-weight:600;margin-bottom:8px}
.why-item p{font-size:15px;line-height:23px}
.why-rule{height:2px;width:132px;background:linear-gradient(90deg,var(--olive) 40%,#ddd 40%)}
.why-graphic{left:386px;top:2410px;width:430px;height:430px;border-radius:50%;background:linear-gradient(160deg,var(--olive) 0%,var(--olive-light) 35%,var(--peach) 60%,var(--plum) 100%)}

/* vacation */
.vacation{top:2902px;left:0;width:1200px;height:454px;background:var(--olive)}
.vac-photo{left:0;top:0;width:760px;height:454px;background:linear-gradient(90deg,#4c6a2e 0%,#6b8a3a 45%,rgba(123,139,16,0) 100%)}
.discount{left:943px;top:2857px;width:96px;height:96px;border-radius:50%;background:#fff;border:4px solid var(--olive);display:flex;flex-direction:column;align-items:center;justify-content:center;color:var(--olive);line-height:1.1}
.discount b{font-size:24px}
.discount span{font-size:14px}
.vac-text{left:589px;top:3000px;width:440px;color:#fff}
.vac-text h2{font-family:'Playfair Display',serif;font-size:34px;margin:4px 0 6px}
.vac-text p{font-size:15.5px;line-height:23px;margin-bottom:14px}

/* pricing */
.plan{top:3505px;width:282px;height:372px;background:#fff;box-shadow:0 4px 24px rgba(0,0,0,.08);text-align:center;color:var(--ink)}
.plan.featured{background:var(--plum);color:#fff}
.plan h5{font-size:15px;font-weight:500;margin-top:22px}
.price{font-weight:700;font-size:36px;margin-top:18px}
.price sup{font-size:16px;vertical-align:18px}
.price small{font-size:11px;font-weight:500}
.plan hr{border:0;border-top:1px solid #e2e2e2;width:236px;margin:14px auto 20px}
.plan.featured hr{border-color:#7a4c5b}
.plan ul{list-style:none;text-align:left;padding-left:56px}
.plan li{display:flex;align-items:center;gap:10px;font-size:15px;height:30.5px}
.plan .btn{left:81px;top:330px;width:120px;height:32px;font-size:11px}

/* reviews */
.review-photo{left:638px;top:3941px;width:562px;height:487px;background:linear-gradient(135deg,#e9e2da 0%,#cdbfb2 50%,#b59b88 100%)}
.avatar{left:359px;top:4067px;width:108px;height:108px;border-radius:50%;background:linear-gradient(#6b4a3c,#c79e86)}
.quote-mark{left:443px;top:4070px;width:40px;height:40px;background:var(--peach);clip-path:polygon(25% 0,75% 0,100% 50%,75% 100%,25% 100%,0 50%);color:#fff;font-family:'Playfair Display',serif;font-size:32px;text-align:center;line-height:48px}
.quote{left:200px;top:4208px;width:430px;text-align:center;font-style:italic;font-weight:500;font-size:15px;line-height:23px;color:var(--ink)}
.arrow{top:4350px;width:42px;height:42px;border-radius:50%;background:var(--plum);display:flex;align-items:center;justify-content:center}

/* newsletter & footer */
.footer{top:4527px;left:0;width:1200px;height:452px;background:var(--plum-dark)}
.newsletter{left:81px;top:4465px;width:1038px;height:122px;background:var(--peach);clip-path:polygon(40px 0,calc(100% - 40px) 0,100% 50%,calc(100% - 40px) 100%,40px 100%,0 50%)}
.news-title{left:134px;top:4484px;font-family:'Playfair Display',serif;color:#fff;font-size:34px;font-weight:700}
.news-sub{left:134px;top:4530px;width:360px;color:#fff;font-size:14px;line-height:22px}
.news-divider{left:505px;top:4490px;width:1px;height:72px;background:#fff}
.news-input{left:531px;top:4505px;width:309px;height:41px;background:#fff;font-size:13px;color:#888;display:flex;align-items:center;padding-left:14px}
.foot-head{font-family:'Playfair Display',serif;color:#fff;font-size:19px;font-weight:700}
.foot-row{display:flex;align-items:center;gap:16px;color:#ddd;font-size:14px;line-height:21px}
.foot-icon{width:42px;height:42px;border-radius:50%;border:1px solid #a67d8a;display:flex;align-items:center;justify-content:center;flex:none}
.sitemap{list-style:none;font-size:14px;color:#ddd}
.sitemap li{height:27px}
.qinput{background:var(--plum);border:1px solid #6d3b4b;color:#cbb;font-size:13px;padding:12px 14px}
.pay{top:4848px;width:46px;height:31px;border-radius:3px}
</style>
</head>
<body>

<!-- navigation -->
<header class="site-nav abs">
  <div class="brand abs"><span class="brand-dot"></span>Whisker Nana</div>
  <span class="nav-links abs" style="left:311px;color:var(--olive)">Home</span>
  <span class="nav-links abs" style="left:373px">About Me</span>
  <span class="nav-links abs" style="left:464px">Service Area</span>
  <span class="nav-links abs" style="left:576px">Pricing</span>
  <span class="nav-links abs" style="left:647px">Vacation Service</span>
  <span class="nav-links abs" style="left:790px">Contact</span>
  <div class="nav-call abs">
    <span class="call-ring"><svg width="18" height="18" viewBox="0 0 24 24" fill="none" stroke="#fff" stroke-width="2"><path d="M5 3h4l2 5-3 2a11 11 0 0 0 6 6l2-3 5 2v4a2 2 0 0 1-2 2A17 17 0 0 1 3 5a2 2 0 0 1 2-2z"/></svg></span>
    <div><small>Need Help:</small><b>415-555-0142</b></div>
  </div>
</header>

<!-- hero -->
<section class="hero abs" role="img" aria-label="Photo of a grandmother cuddling a hairless cat on a bed"></section>
<h1 class="hero-title abs serif" style="color:#fff">Cat Sitting Services<br>in Marin &amp; Sonoma</h1>
<p class="hero-lead abs">Lorem ipsum dolor sit amet consectetur adipiscing elit sed do eiusmod tempor</p>
<a class="btn btn-peach" style="left:160px;top:459px;width:242px;height:42px">Ask For a Free Consultation</a>

<form class="reserve abs">
  <h3>Reservation Request</h3>
  <label>Full Name *</label><div class="field">Enter your name</div>
  <label>Phone No *</label><div class="field">Enter phone no</div>
  <label>Booking Date *</label><div class="field">Choose your date
    <svg width="12" height="12" viewBox="0 0 12 12"><rect x="1" y="2" width="10" height="9" fill="#777"/><rect x="2" y="5" width="8" height="5" fill="#fff"/></svg></div>
  <label>Booking Time *</label><div class="field">Morning 8AM- Noon or Afternoon
    <svg width="10" height="10" viewBox="0 0 10 10"><path d="M1 3l4 4 4-4" fill="none" stroke="#555" stroke-width="1.5"/></svg></div>
  <a class="btn btn-peach">Reserve Your Request
    <svg width="14" height="12" viewBox="0 0 14 12"><path d="M1 6h11M8 2l4 4-4 4" fill="none" stroke="#fff" stroke-width="2"/></svg></a>
</form>

<!-- contact strip -->
<div class="contact-line abs"></div>
<div class="contact-item abs" style="left:158px">
  <span class="ring"><svg width="18" height="14" viewBox="0 0 18 14" fill="none" stroke="#fff" stroke-width="1.6"><rect x="1" y="1" width="16" height="12" rx="1"/><path d="M1 2l8 6 8-6"/></svg></span>
  <div>Email Me:<b>hello@whiskernana.com</b></div>
</div>
<div class="contact-item abs" style="left:390px">
  <span class="ring"><svg width="18" height="18" viewBox="0 0 24 24" fill="none" stroke="#fff" stroke-width="2"><path d="M5 3h4l2 5-3 2a11 11 0 0 0 6 6l2-3 5 2v4a2 2 0 0 1-2 2A17 17 0 0 1 3 5a2 2 0 0 1 2-2z"/></svg></span>
  <div>Need Help Call Me:<b style="font-size:16px;letter-spacing:.5px">415-555-0142</b></div>
</div>

<!-- about -->
<div class="portrait abs" role="img" aria-label="Portrait photo of the cat sitter, a smiling grandmother"></div>
<div class="portrait-band abs"><span class="sig">Marla Finch</span><div><b>Expert In</b><span>Professional Cat Care</span></div></div>

<section class="who abs">
  <div class="eyebrow">Introduction</div>
  <h2 class="serif">Who I Am</h2>
  <p>Duis aute irure dolor in reprehenderit in voluptate velit esse cillum dolore eu fugiat nulla pariatur. Excepteur ill sint occaecat cupidatat non proident, sunt in culpa qui officia deserunt mollit anim id est</p>
  <ul class="checks">
    <li><svg width="16" height="12" viewBox="0 0 16 12"><path d="M1 6l5 5L15 1" fill="none" stroke="var(--olive)" stroke-width="2.5"/></svg>Professional Cat Caring</li>
    <li><svg width="16" height="12" viewBox="0 0 16 12"><path d="M1 6l5 5L15 1" fill="none" stroke="var(--olive)" stroke-width="2.5"/></svg>100% Trustworth</li>
    <li><svg width="16" height="12" viewBox="0 0 16 12"><path d="M1 6l5 5L15 1" fill="none" stroke="var(--olive)" stroke-width="2.5"/></svg>Reasonable &amp; Affordable Price</li>
  </ul>
  <h4>Qualifications Summary</h4>
  <div class="quals">
    <div><b>Higher Education :</b><br>Excepteur ill sint occaecat sun quiet cupidatat non proident</div>
    <div><b>Bachelor's Degree</b><br>Occaecat quiet cupidata non proident sunt in.</div>
  </div>
</section>
<a class="btn btn-peach" style="left:609px;top:1435px;width:158px;height:44px">More About Us</a>
<div class="cat-peek abs" role="img" aria-label="Photo of a tabby kitten raising a paw"></div>

<!-- services -->
<section class="services abs"></section>
<div class="abs center eyebrow" style="top:1635px">What I Do?</div>
<h2 class="abs center serif" style="top:1652px;font-size:34px">Provide The Best Services</h2>

<article class="card abs" style="left:158px">
  <div class="card-photo" role="img" aria-label="Photo of a woman hugging a ginger cat" style="background:linear-gradient(135deg,#f3d9c6,#d99a6a)"></div>
  <svg class="card-v" viewBox="0 0 207 38"><path d="M0 3 L103.5 35 L207 3" fill="none" stroke="var(--plum)" stroke-width="5"/></svg>
  <h3>Cat Grooming</h3><p>Sed do eiusmod ad tempor incididunt ut labore et</p>
  <a class="btn btn-olive">View More</a>
</article>
<article class="card abs" style="left:384px">
  <div class="card-photo" role="img" aria-label="Photo of a woman in a chair holding a grey cat" style="background:linear-gradient(135deg,#f1eee9,#b7aca0)"></div>
  <svg class="card-v" viewBox="0 0 207 38"><path d="M0 3 L103.5 35 L207 3" fill="none" stroke="var(--plum)" stroke-width="5"/></svg>
  <h3>Cat Sitting</h3><p>Sed do eiusmod ad tempor incididunt ut labore et</p>
  <a class="btn btn-olive">View More</a>
</article>
<article class="card abs" style="left:609px">
  <div class="card-photo" role="img" aria-label="Photo of a ginger and white cat eating from a bowl" style="background:linear-gradient(135deg,#f5f2ee,#d8a070)"></div>
  <svg class="card-v" viewBox="0 0 207 38"><path d="M0 3 L103.5 35 L207 3" fill="none" stroke="var(--plum)" stroke-width="5"/></svg>
  <h3>Healthy Meals</h3><p>Sed do eiusmod ad tempor incididunt ut labore et</p>
  <a class="btn btn-olive">View More</a>
</article>
<article class="card abs" style="left:833px">
  <div class="card-photo" role="img" aria-label="Photo of a veterinarian examining a cat" style="background:linear-gradient(135deg,#d8e6e6,#3f8a86)"></div>
  <svg class="card-v" viewBox="0 0 207 38"><path d="M0 3 L103.5 35 L207 3" fill="none" stroke="var(--plum)" stroke-width="5"/></svg>
  <h3>Veterinary</h3><p>Sed do eiusmod ad tempor incididunt ut labore et</p>
  <a class="btn btn-olive">View More</a>
</article>
<div class="abs" style="left:524px;top:2118px;font-size:13px;font-weight:600;color:var(--ink);text-decoration:underline;display:flex;gap:8px;align-items:center">View All Services
  <svg width="14" height="12" viewBox="0 0 14 12"><path d="M1 6h11M8 2l4 4-4 4" fill="none" stroke="var(--ink)" stroke-width="2"/></svg></div>

<!-- why book me -->
<div class="abs center eyebrow" style="top:2256px">Reason To Choose</div>
<h2 class="abs center serif" style="top:2274px;font-size:34px">Why Book Me?</h2>
<p class="abs" style="left:400px;top:2326px;width:400px;text-align:center;font-size:15px;line-height:23px">Duis aute irure dolor in reprehenderit in voluptate velit esse cillum dolore eu fugiat nulla pariatur.</p>

<div class="why-item abs" style="left:158px;top:2484px"><h4>14+Years Experience</h4><p>Voluptate velit esse cillum dolore eu fugiat nulla sed pariatur sunt</p></div>
<div class="why-rule abs" style="left:158px;top:2625px"></div>
<div class="why-item abs" style="left:158px;top:2668px"><h4>Certified Groomer</h4><p>Voluptate velit esse cillum dolore eu fugiat nulla sed pariatur sunt</p></div>
<div class="why-item abs" style="left:833px;top:2484px"><h4>Monthly Care</h4><p>Voluptate velit esse cillum dolore eu fugiat nulla sed pariatur sunt</p></div>
<div class="why-rule abs" style="left:833px;top:2625px"></div>
<div class="why-item abs" style="left:833px;top:2668px"><h4>Pet Adoption</h4><p>Voluptate velit esse cillum dolore eu fugiat nulla sed pariatur sunt</p></div>

<div class="why-graphic abs" role="img" aria-label="Decorative swirl graphic in olive, peach and plum with service icons around a grandmother and cat illustration"></div>

<!-- vacation -->
<section class="vacation abs">
  <div class="vac-photo abs" role="img" aria-label="Photo of a tabby cat lying on a blue table outdoors"></div>
</section>
<div class="discount abs"><b>5%</b><span>Discount</span></div>
<div class="vac-text abs">
  <div style="font-size:12px;font-weight:600">Special Service</div>
  <h2>Vacation Services</h2>
  <p>Duis aute irure dolor in reprehenderit in voluptate velit esse cillum dolore eu fugiat nulla pariatur. Excepteur ill sint occaecat cupidatat non proident,</p>
  <p>Duis aute irure dolor in reprehenderit in voluptate velit esse cillum dolore eu fugiat nulla pariatur.</p>
</div>
<a class="btn btn-peach" style="left:589px;top:3219px;width:206px;height:42px;font-size:12px">More Special Services</a>

<!-- pricing -->
<div class="abs center eyebrow" style="top:3409px">Pricing</div>
<h2 class="abs center serif" style="top:3428px;font-size:34px">My Services Rate</h2>

<div class="plan abs" style="left:158px">
  <h5>Day Care Services</h5>
  <div class="price"><sup>$</sup>150 <small>/month</small></div><hr>
  <ul>
    <li><svg width="16" height="16" viewBox="0 0 16 16"><circle cx="8" cy="8" r="8" fill="var(--olive)"/><path d="M4 8l3 3 5-6" fill="none" stroke="#fff" stroke-width="2"/></svg>Grooming 2x</li>
    <li><svg width="16" height="16" viewBox="0 0 16 16"><circle cx="8" cy="8" r="8" fill="var(--olive)"/><path d="M4 8l3 3 5-6" fill="none" stroke="#fff" stroke-width="2"/></svg>Socialist Exercise</li>
    <li><svg width="16" height="16" viewBox="0 0 16 16"><circle cx="8" cy="8" r="8" fill="var(--olive)"/><path d="M4 8l3 3 5-6" fill="none" stroke="#fff" stroke-width="2"/></svg>Custom Meals</li>
    <li><svg width="16" height="16" viewBox="0 0 16 16"><circle cx="8" cy="8" r="8" fill="var(--olive)"/><path d="M4 8l3 3 5-6" fill="none" stroke="#fff" stroke-width="2"/></svg>Spa and Grooming</li>
    <li><svg width="16" height="16" viewBox="0 0 16 16"><circle cx="8" cy="8" r="8" fill="var(--olive)"/><path d="M4 8l3 3 5-6" fill="none" stroke="#fff" stroke-width="2"/></svg>Excercise 2x</li>
  </ul>
  <a class="btn btn-peach">Buy Now</a>
</div>
<div class="plan featured abs" style="left:458px">
  <h5>2X Care Services</h5>
  <div class="price"><sup>$</sup>199 <small>/month</small></div><hr>
  <ul>
    <li><svg width="16" height="16" viewBox="0 0 16 16"><circle cx="8" cy="8" r="8" fill="var(--olive)"/><path d="M4 8l3 3 5-6" fill="none" stroke="#fff" stroke-width="2"/></svg>Grooming 2x</li>
    <li><svg width="16" height="16" viewBox="0 0 16 16"><circle cx="8" cy="8" r="8" fill="var(--olive)"/><path d="M4 8l3 3 5-6" fill="none" stroke="#fff" stroke-width="2"/></svg>Socialist Exercise</li>
    <li><svg width="16" height="16" viewBox="0 0 16 16"><circle cx="8" cy="8" r="8" fill="var(--olive)"/><path d="M4 8l3 3 5-6" fill="none" stroke="#fff" stroke-width="2"/></svg>Custom Meals</li>
    <li><svg width="16" height="16" viewBox="0 0 16 16"><circle cx="8" cy="8" r="8" fill="var(--olive)"/><path d="M4 8l3 3 5-6" fill="none" stroke="#fff" stroke-width="2"/></svg>Spa and Grooming</li>
    <li><svg width="16" height="16" viewBox="0 0 16 16"><circle cx="8" cy="8" r="8" fill="var(--olive)"/><path d="M4 8l3 3 5-6" fill="none" stroke="#fff" stroke-width="2"/></svg>Excercise 2x</li>
  </ul>
  <a class="btn btn-olive">Buy Now</a>
</div>
<div class="plan abs" style="left:757px">
  <h5>4X Care Services</h5>
  <div class="price"><sup>$</sup>250 <small>/month</small></div><hr>
  <ul>
    <li><svg width="16" height="16" viewBox="0 0 16 16"><circle cx="8" cy="8" r="8" fill="var(--olive)"/><path d="M4 8l3 3 5-6" fill="none" stroke="#fff" stroke-width="2"/></svg>Grooming 4x</li>
    <li><svg width="16" height="16" viewBox="0 0 16 16"><circle cx="8" cy="8" r="8" fill="var(--olive)"/><path d="M4 8l3 3 5-6" fill="none" stroke="#fff" stroke-width="2"/></svg>Socialist Exercise</li>
    <li><svg width="16" height="16" viewBox="0 0 16 16"><circle cx="8" cy="8" r="8" fill="var(--olive)"/><path d="M4 8l3 3 5-6" fill="none" stroke="#fff" stroke-width="2"/></svg>Custom Meals</li>
    <li><svg width="16" height="16" viewBox="0 0 16 16"><circle cx="8" cy="8" r="8" fill="var(--olive)"/><path d="M4 8l3 3 5-6" fill="none" stroke="#fff" stroke-width="2"/></svg>Spa and Grooming</li>
    <li><svg width="16" height="16" viewBox="0 0 16 16"><circle cx="8" cy="8" r="8" fill="var(--olive)"/><path d="M4 8l3 3 5-6" fill="none" stroke="#fff" stroke-width="2"/></svg>Excercise 4x</li>
  </ul>
  <a class="btn btn-peach">Buy Now</a>
</div>

<!-- reviews -->
<div class="review-photo abs" role="img" aria-label="Photo of a smiling woman holding a hairless cat"></div>
<div class="abs eyebrow" style="left:158px;top:3986px">Testimonials</div>
<h2 class="abs serif" style="left:158px;top:4004px;font-size:34px">Client Reviews</h2>
<div class="avatar abs" role="img" aria-label="Client portrait photo"></div>
<div class="quote-mark abs">“</div>
<p class="quote abs">Duis aute irure dolor in reprehenderit in voluptate velit esse cillum dolore eu fugiat nulla pariatur. Excepteur ill sint occaecat cupidatat non proident sunt in culpa sid</p>
<div class="abs serif" style="left:200px;top:4306px;width:430px;text-align:center;color:var(--olive);font-size:19px">Nora Bell</div>
<span class="arrow abs" style="left:375px"><svg width="12" height="14" viewBox="0 0 12 14"><path d="M9 1L3 7l6 6" fill="none" stroke="#fff" stroke-width="2"/></svg></span>
<span class="arrow abs" style="left:427px"><svg width="12" height="14" viewBox="0 0 12 14"><path d="M3 1l6 6-6 6" fill="none" stroke="#fff" stroke-width="2"/></svg></span>

<!-- footer -->
<footer class="footer abs"></footer>
<div class="newsletter abs"></div>
<div class="news-title abs">Signup For Newsletter</div>
<p class="news-sub abs">Lorem ipsum dolor sit amet consectetur adi pisicing elit sed do eiusmod tempor.</p>
<div class="news-divider abs"></div>
<div class="news-input abs">Enter your name</div>
<a class="btn btn-olive btn-pill" style="left:862px;top:4505px;width:195px;height:41px">Subscribe Now
  <svg width="14" height="12" viewBox="0 0 14 12"><path d="M1 6h11M8 2l4 4-4 4" fill="none" stroke="#fff" stroke-width="2"/></svg></a>

<div class="foot-head abs" style="left:158px;top:4620px">Contact Information</div>
<div class="foot-row abs" style="left:158px;top:4663px">
  <span class="foot-icon"><svg width="14" height="18" viewBox="0 0 14 18" fill="none" stroke="#fff" stroke-width="1.6"><path d="M7 17s6-6 6-10A6 6 0 0 0 1 7c0 4 6 10 6 10z"/><circle cx="7" cy="7" r="2"/></svg></span>
  <span>Lorem ipsum dolor sit<br>sed do eiusmod</span>
</div>
<div class="foot-row abs" style="left:158px;top:4724px">
  <span class="foot-icon"><svg width="16" height="14" viewBox="0 0 16 14" fill="none" stroke="#fff" stroke-width="1.6"><path d="M1 7l7-6 7 6M3 6v7h10V6"/></svg></span>
  <span>hello@whiskernana.com</span>
</div>
<div class="foot-row abs" style="left:158px;top:4782px">
  <span class="foot-icon"><svg width="16" height="16" viewBox="0 0 24 24" fill="none" stroke="#fff" stroke-width="2"><path d="M5 3h4l2 5-3 2a11 11 0 0 0 6 6l2-3 5 2v4a2 2 0 0 1-2 2A17 17 0 0 1 3 5a2 2 0 0 1 2-2z"/></svg></span>
  <span>415-555-0142</span>
</div>
<div class="pay abs" style="left:158px;background:#fff"></div>
<div class="pay abs" style="left:210px;background:#f0f0f0"></div>
<div class="pay abs" style="left:262px;background:#e6e6e6"></div>
<div class="pay abs" style="left:314px;background:#dcdcdc"></div>
<div class="abs" style="left:158px;top:4915px;font-size:12px;color:#ccc">© 2021 Whisker Nana.</div>

<div class="foot-head abs" style="left:435px;top:4620px">Sitemap</div>
<ul class="sitemap abs" style="left:435px;top:4662px">
  <li>Home</li><li>About Me</li><li>Service Area</li><li>Pricing</li><li>Vacation Service</li><li>Contact Me</li><li>Cancellation Policy</li><li>View Map</li>
</ul>

<div class="foot-head abs" style="left:618px;top:4620px">Quick Contact</div>
<div class="qinput abs" style="left:618px;top:4666px;width:207px;height:41px">Name</div>
<div class="qinput abs" style="left:833px;top:4666px;width:207px;height:41px">Email</div>
<div class="qinput abs" style="left:618px;top:4718px;width:422px;height:41px">Phone</div>
<div class="qinput abs" style="left:618px;top:4770px;width:422px;height:105px">Leave your message</div>
<a class="btn btn-olive" style="left:618px;top:4888px;width:165px;height:39px">Submit Now
  <svg width="14" height="12" viewBox="0 0 14 12"><path d="M1 6h11M8 2l4 4-4 4" fill="none" stroke="#fff" stroke-width="2"/></svg></a>

</body>
</html>
```